Brightmoor Deed Partners Stationery
BDP Stationery
Brightmoor Deed Partners Stationery - Real Estate
Creative Brief
Professional
Leopoldo Varnhusk II
Manager
4817 North Kettleridge Road, Suite 320 Coconut Grove, Florida 33187
lv@brightmoordeedpartners.example
www.brightmoordeedpartners.example
$100 bonus to winning designer upon designer creating duplicate design and stationery for "Brightmoor Deed Alliance"

```html
<!DOCTYPE html>
<html lang="en">
<head>
<meta charset="utf-8">
<title>Brightmoor Deed Partners Stationery</title>
<link rel="stylesheet" href="https://fonts.googleapis.com/css2?family=Open+Sans:wght@300;400;600&display=swap">
<style>
  :root {
    --page-bg: #ececec;
    --card-white: #ffffff;
    --card-dark: #2e3036;
    --ink: #2b2b2b;
    --ink-soft: #6b6b6b;
    --on-dark: #f2f2f2;
    --on-dark-soft: #a9abb0;
    --accent-green: #5cb84a;
    --rule: #c8c8c8;
  }
  * { box-sizing: border-box; margin: 0; padding: 0; }
  html, body { width: 1200px; height: 901px; overflow: hidden; }
  body {
    background: var(--page-bg);
    font-family: "Open Sans", Arial, sans-serif;
    position: relative;
  }
  .card {
    position: absolute;
    width: 660px;
    height: 377px;
    box-shadow: 0 10px 30px rgba(0,0,0,0.12);
  }
  .card-front { left: 150px; top: 60px; background: var(--card-white); color: var(--ink); }
  .card-back  { left: 390px; top: 464px; background: var(--card-dark); color: var(--on-dark); }

  .brand { display: flex; align-items: center; gap: 12px; white-space: nowrap; }
  .brand-mark { width: 22px; height: 22px; background: var(--accent-green); flex: none; }
  .brand-name { font-weight: 600; text-transform: uppercase; letter-spacing: 0.04em; line-height: 1; }

  .card-front .brand { position: absolute; left: 44px; top: 56px; }
  .card-front .brand-name { font-size: 16px; color: var(--ink); }

  .holder { position: absolute; right: 44px; top: 50px; text-align: right; white-space: nowrap; }
  .holder-name { font-size: 19px; font-weight: 400; }
  .holder-title { font-size: 13px; color: var(--ink-soft); margin-top: 4px; }

  .rule { position: absolute; left: 44px; right: 44px; top: 150px; height: 1px; background: var(--rule); }

  .contact { position: absolute; font-size: 11.5px; line-height: 1.75; color: var(--ink-soft); white-space: nowrap; }
  .contact-address { left: 44px; bottom: 44px; }
  .contact-online { right: 44px; bottom: 44px; text-align: right; }
  .contact-line { display: flex; align-items: center; gap: 8px; }
  .contact-online .contact-line { justify-content: flex-end; }
  .contact-line svg { width: 11px; height: 11px; flex: none; }

  .back-center {
    position: absolute; left: 0; right: 0; top: 148px;
    display: flex; flex-direction: column; align-items: center; gap: 22px;
  }
  .card-back .brand { gap: 16px; }
  .card-back .brand-mark { width: 34px; height: 34px; }
  .card-back .brand-name { font-size: 26px; color: var(--on-dark); }
  .back-web { font-size: 12px; letter-spacing: 0.03em; color: var(--on-dark-soft); }
</style>
</head>
<body>
  <section class="card card-front" aria-label="Business card front">
    <div class="brand">
      <span class="brand-mark"></span>
      <span class="brand-name">Brightmoor Deed Alliance</span>
    </div>
    <div class="holder">
      <p class="holder-name">Leopoldo Varnhusk II</p>
      <p class="holder-title">Manager</p>
    </div>
    <div class="rule"></div>
    <div class="contact contact-address">
      <p class="contact-line">4817 North Kettleridge Road, Suite 320</p>
      <p class="contact-line">Coconut Grove, Florida 33187</p>
      <p class="contact-line">T 305.555.0142</p>
      <p class="contact-line">F 305.555.0178</p>
    </div>
    <div class="contact contact-online">
      <p class="contact-line">
        <svg viewBox="0 0 12 12"><rect x="1" y="2.5" width="10" height="7" fill="none" stroke="#5cb84a" stroke-width="1.2"/><path d="M1 3l5 4 5-4" fill="none" stroke="#5cb84a" stroke-width="1.2"/></svg>
        lv@brightmoordeedpartners.example
      </p>
      <p class="contact-line">
        <svg viewBox="0 0 12 12"><circle cx="6" cy="6" r="4.8" fill="none" stroke="#5cb84a" stroke-width="1.2"/><path d="M1.2 6h9.6M6 1.2c-2.4 3-2.4 6.6 0 9.6M6 1.2c2.4 3 2.4 6.6 0 9.6" fill="none" stroke="#5cb84a" stroke-width="1"/></svg>
        www.brightmoordeedpartners.example
      </p>
    </div>
  </section>

  <section class="card card-back" aria-label="Business card back">
    <div class="back-center">
      <div class="brand">
        <span class="brand-mark"></span>
        <span class="brand-name">Brightmoor Deed Alliance</span>
      </div>
      <p class="back-web">www.brightmoordeedpartners.example</p>
    </div>
  </section>
</body>
</html>
```